Graphic Design for Nookle packaging (Nookle.net)

Nookle is a brand name of self adhesive universal tablet computer wall mounting solution, primary intended for all Orbel vSlates. Nookles are made from a special self adhesive "klemmo" material and adhesive. You can find out more on www.nookle-mounts.example

```html
<!DOCTYPE html>
<html lang="en">
<head>
<meta charset="utf-8">
<title>Nookle packaging dieline</title>
<link rel="stylesheet" href="https://fonts.googleapis.com/css2?family=Open+Sans:wght@400;700;800&family=PT+Sans+Narrow:wght@400;700&display=swap">
<style>
  :root {
    --backdrop: #c9ab85;
    --board-black: #0b0b0b;
    --board-white: #ffffff;
    --accent-yellow: #f7cd0c;
    --brand-grey: #8c8c8c;
    --text-white: #f2f2f2;
    --text-dark: #111111;
  }
  html, body {
    margin: 0;
    padding: 0;
    width: 1200px;
    height: 951px;
    overflow: hidden;
    background: var(--backdrop);
  }
  .canvas {
    position: relative;
    width: 1200px;
    height: 951px;
    overflow: hidden;
    background: var(--backdrop);
  }
  .dieline {
    position: absolute;
    left: 0;
    top: 0;
    width: 900px;
    height: 713px;
    transform: scale(1.33334);
    transform-origin: 0 0;
  }
  .dieline svg {
    position: absolute;
    left: 0;
    top: 0;
  }
  .brand-mark {
    position: absolute;
    font-family: "PT Sans Narrow", sans-serif;
    font-weight: 700;
    color: var(--text-dark);
    letter-spacing: 0.5px;
  }
  .brand-mark--top {
    left: 352px;
    top: 80px;
    font-size: 20px;
  }
  .brand-mark--bottom {
    left: 432px;
    top: 677px;
    font-size: 14px;
    color: var(--brand-grey);
  }
  .side-copy {
    position: absolute;
    left: 190px;
    top: 139px;
    width: 122px;
    font-family: "Open Sans", sans-serif;
    font-size: 5.6px;
    line-height: 1.5;
    color: var(--text-white);
  }
  .side-copy p {
    margin: 0 0 8px;
  }
  .side-copy strong {
    font-weight: 700;
  }
  .front-wordmark {
    position: absolute;
    right: 330px;
    top: 133px;
    font-family: "Open Sans", sans-serif;
    font-weight: 800;
    font-size: 36px;
    letter-spacing: 1px;
    color: var(--brand-grey);
    line-height: 1;
  }
  .front-headline {
    position: absolute;
    left: 342px;
    top: 178px;
    margin: 0;
    font-family: "PT Sans Narrow", sans-serif;
    font-weight: 700;
    font-size: 15px;
    line-height: 23px;
    color: var(--text-white);
    letter-spacing: 0.3px;
  }
  .piece-count {
    position: absolute;
    left: 323px;
    top: 325px;
    width: 72px;
    height: 60px;
    background: var(--accent-yellow);
    border-top-right-radius: 8px;
    font-family: "PT Sans Narrow", sans-serif;
    font-weight: 700;
    color: var(--text-dark);
    text-align: center;
    line-height: 1;
  }
  .piece-count__number {
    display: block;
    font-size: 20px;
    margin-top: 9px;
  }
  .piece-count__label {
    display: block;
    font-size: 16px;
  }
  .contents-note {
    position: absolute;
    left: 401px;
    top: 348px;
    width: 180px;
    font-family: "Open Sans", sans-serif;
    font-size: 5.6px;
    line-height: 1.35;
    color: var(--text-white);
  }
  .back-wordmark {
    position: absolute;
    left: 330px;
    top: 608px;
    font-family: "Open Sans", sans-serif;
    font-weight: 800;
    font-size: 36px;
    letter-spacing: 1px;
    color: var(--brand-grey);
    line-height: 1;
    transform: rotate(180deg);
  }
</style>
</head>
<body>
<div class="canvas">
  <div class="dieline">
    <svg width="900" height="713" viewBox="0 0 900 713" xmlns="http://www.w3.org/2000/svg">
      <defs>
        <radialGradient id="glow" cx="0.5" cy="0.5" r="0.5">
          <stop offset="0" stop-color="#ffffff"/>
          <stop offset="0.3" stop-color="#b5b5b5"/>
          <stop offset="0.7" stop-color="#3a3a3a"/>
          <stop offset="1" stop-color="#0b0b0b"/>
        </radialGradient>
        <linearGradient id="mountsTone" x1="0" y1="0" x2="1" y2="0">
          <stop offset="0" stop-color="#1f2430"/>
          <stop offset="0.5" stop-color="#6e6e6e"/>
          <stop offset="1" stop-color="#f0f0f0"/>
        </linearGradient>
        <linearGradient id="tileGrey" x1="0" y1="0" x2="1" y2="1">
          <stop offset="0" stop-color="#f4f4f4"/>
          <stop offset="1" stop-color="#8e8e8e"/>
        </linearGradient>
        <linearGradient id="tileYellow" x1="0" y1="0" x2="1" y2="1">
          <stop offset="0" stop-color="#f7cd0c"/>
          <stop offset="1" stop-color="#e9c10a"/>
        </linearGradient>
        <clipPath id="rightFlapClip">
          <rect x="590" y="130" width="125" height="225"/>
        </clipPath>
        <clipPath id="frontPanelClip">
          <rect x="323" y="130" width="265" height="255"/>
        </clipPath>
      </defs>

      <!-- left side flap -->
      <polygon class="flap-tuck" points="185,88 200,72 318,72 318,130 185,130" fill="var(--board-white)"/>
      <rect class="flap-body" x="185" y="130" width="133" height="225" fill="var(--board-black)"/>
      <polygon class="flap-band" points="185,355 318,355 318,385 200,385 185,370" fill="var(--accent-yellow)"/>

      <!-- right side flap -->
      <polygon class="flap-tuck" points="590,72 700,72 715,88 715,130 590,130" fill="var(--board-white)"/>
      <rect class="flap-body" x="590" y="130" width="125" height="225" fill="var(--board-black)"/>
      <g clip-path="url(#rightFlapClip)">
        <circle cx="690" cy="240" r="86" fill="#3c3c3c" role="img" aria-label="Large hedgehog silhouette inside a grey disc"/>
      </g>
      <polygon class="flap-band" points="590,355 715,355 715,370 700,385 590,385" fill="var(--accent-yellow)"/>

      <!-- front lid dome -->
      <path class="lid-dome" d="M323,130 L323,62 C323,22 380,2 455,2 C530,2 588,22 588,62 L588,130 Z" fill="var(--board-white)"/>
      <rect class="hang-tab" x="413" y="6" width="57" height="30" rx="12" fill="#fafafa" stroke="#d6d6d6" stroke-width="1"/>

      <!-- front panel -->
      <rect class="front-panel" x="323" y="130" width="265" height="255" fill="var(--board-black)"/>
      <g clip-path="url(#frontPanelClip)">
        <circle cx="470" cy="240" r="118" fill="url(#glow)" role="img" aria-label="Glowing backdrop with a hedgehog silhouette"/>
      </g>
      <ellipse cx="502" cy="302" rx="68" ry="28" fill="url(#mountsTone)" role="img" aria-label="One black and one white round wall mount"/>

      <!-- back panel -->
      <rect class="back-panel" x="323" y="385" width="265" height="267" fill="var(--board-black)"/>
      <rect x="350" y="410" width="93" height="90" fill="url(#tileGrey)" role="img" aria-label="Step 3: tablet hanging on the wall mount"/>
      <rect x="452" y="410" width="116" height="90" fill="url(#tileGrey)" role="img" aria-label="Step 4: tablet pressed onto the wall mount"/>
      <rect x="350" y="508" width="93" height="92" fill="url(#tileYellow)" role="img" aria-label="Step 2: fixing attached to the back of the tablet"/>
      <rect x="452" y="508" width="116" height="92" fill="url(#tileGrey)" role="img" aria-label="Step 1: mount pressed onto a tiled wall"/>

      <rect class="back-band" x="323" y="652" width="265" height="15" fill="var(--accent-yellow)"/>
      <path class="base-dome" d="M323,667 L588,667 L588,690 C588,705 530,713 455,713 C380,713 323,705 323,690 Z" fill="var(--board-white)"/>
    </svg>

    <div class="brand-mark brand-mark--top">Nookle</div>

    <div class="side-copy">
      <p><strong>Nookle</strong> lets you mount your tablet on the wall, glass, tiles, wood, plastic, metal and other surface, where you want it and when you want it. Therefore it gives you freedom to enjoy your tablet without holding it.</p>
      <p>With just a gentle press your tablet will be safely mounted in a portrait or landscape orientation, to enjoy movies or cartoons, watch instructional videos while cooking or making repairs, use it as digital photo frame, etc.</p>
      <p><strong>Nookles</strong> are made from a carefully balanced and extremely durable, special self adhesive hook &amp; loop material.</p>
      <p>Materials of the highest quality assures a safe and stable grip of your tablet and protects it's back from scratches.</p>
      <p><strong>Nookle</strong> is so thin, that vSlate or other tablet will still fit in all of your accessories you might already own.</p>
    </div>

    <div class="front-wordmark">NOOKLE</div>
    <h1 class="front-headline">MOUNTING<br>SOLUTION<br>FOR VSLATE OR<br>OTHER TABLETS</h1>

    <div class="piece-count">
      <span class="piece-count__number">4</span>
      <span class="piece-count__label">pieces</span>
    </div>

    <div class="contents-note">self adhesive wall mounts, one black and one white,<br>made from the hook side material and black<br>self adhesive fixing for your device made from loop side material.</div>

    <div class="back-wordmark">NOOKLE</div>
    <div class="brand-mark brand-mark--bottom">Nookle</div>
  </div>
</div>
</body>
</html>
```